Women's Health Company needs business card

We need a business card for a USA based women's health care company. We use digital technology to enhance therapy prescribed by clinicians for their patients

```html
<!DOCTYPE html>
<html lang="en">
<head>
<meta charset="utf-8">
<title>Velora Health – Business Card</title>
<link rel="stylesheet" href="https://fonts.googleapis.com/css2?family=Poppins:wght@300;400&display=swap">
<style>
  :root {
    --backdrop: #363636;
    --card-dark: #1b1c1e;
    --card-light: #2b2c2f;
    --emboss: #0f1011;
    --teal: #5fb0aa;
    --purple: #7d4b94;
    --text-light: #e4e4e4;
  }
  * { margin: 0; padding: 0; box-sizing: border-box; }
  html, body {
    width: 1200px; height: 1138px; overflow: hidden;
    background: var(--backdrop);
    font-family: "Poppins", sans-serif;
  }
  .card {
    position: absolute;
    border-radius: 16px;
    overflow: hidden;
    background: linear-gradient(160deg, var(--card-dark) 0%, var(--card-dark) 45%, var(--card-light) 100%);
  }
  .card-front { left: 272px; top: 184px; width: 622px; height: 376px; }
  .card-back  { left: 274px; top: 606px; width: 618px; height: 375px; }

  .brand { display: flex; align-items: center; gap: 10px; font-weight: 400; white-space: nowrap; }
  .brand-dot { border-radius: 50%; flex: none; }

  .front-brand {
    position: absolute; left: 0; right: 0; top: 140px;
    justify-content: center;
    font-size: 56px; color: var(--emboss); letter-spacing: 1px;
  }
  .front-brand .brand-dot { width: 14px; height: 14px; background: var(--emboss); }

  .front-web {
    position: absolute; left: 98px; width: 428px; top: 320px;
    display: flex; align-items: center; justify-content: space-between;
  }
  .front-web .rule { width: 50px; height: 2px; background: var(--teal); }
  .front-web .url {
    font-size: 15px; font-weight: 300; letter-spacing: 4.4px;
    color: var(--purple);
  }

  .back-brand {
    position: absolute; right: 34px; top: 92px;
    font-size: 40px; color: var(--teal);
  }
  .back-brand .brand-dot { width: 10px; height: 10px; background: var(--purple); }

  .person { position: absolute; left: 35px; top: 196px; }
  .person-name { font-size: 27px; font-weight: 400; color: var(--teal); line-height: 1.2; }
  .person-role { font-size: 16px; font-weight: 400; color: var(--text-light); margin-top: 2px; }

  .contacts { position: absolute; left: 43px; top: 274px; list-style: none; }
  .contacts li {
    display: flex; align-items: center; height: 27px;
    font-size: 16px; font-weight: 300; color: var(--text-light);
  }
  .contacts svg { width: 14px; height: 14px; margin-right: 10px; flex: none; }

  .address {
    position: absolute; right: 33px; top: 296px;
    text-align: right; font-size: 16px; font-weight: 300; line-height: 26px;
    color: var(--text-light); font-style: normal;
  }

  .color-band { position: absolute; left: 0; right: 0; bottom: 0; height: 10px; display: flex; }
  .color-band span { flex: 1; }
  .color-band .band-teal { background: var(--teal); }
  .color-band .band-purple { background: var(--purple); }
</style>
</head>
<body>
  <section class="card card-front" aria-label="Card front">
    <div class="brand front-brand"><span class="brand-dot"></span>Velora Health</div>
    <div class="front-web">
      <span class="rule"></span>
      <span class="url">www.velorahealth.com</span>
      <span class="rule"></span>
    </div>
  </section>

  <section class="card card-back" aria-label="Card back">
    <div class="brand back-brand"><span class="brand-dot"></span>Velora Health</div>

    <div class="person">
      <p class="person-name">Mark Delane</p>
      <p class="person-role">Health Advisor</p>
    </div>

    <ul class="contacts">
      <li>
        <svg viewBox="0 0 16 16" aria-hidden="true"><path fill="#7d4b94" d="M2 5c0-2 3-3 6-3s6 1 6 3v1.5h-3V5H5v1.5H2zM4 8l2-2h4l2 2v6H4z"/><circle cx="8" cy="10.5" r="1.6" fill="#1b1c1e"/></svg>
        00-000-0000
      </li>
      <li>
        <svg viewBox="0 0 16 16" aria-hidden="true"><rect x="1" y="3" width="14" height="10" rx="1" fill="#5fb0aa"/><path d="M1.5 3.5 8 9l6.5-5.5M1.5 12.5 6 7.5M14.5 12.5 10 7.5" stroke="#1b1c1e" stroke-width="1.2" fill="none"/></svg>
        mark@velorahealth.com
      </li>
      <li>
        <svg viewBox="0 0 16 16" aria-hidden="true"><circle cx="8" cy="8" r="6.5" fill="#7d4b94"/><path d="M1.5 8h13M8 1.5c-2.5 3-2.5 10 0 13M8 1.5c2.5 3 2.5 10 0 13" stroke="#1b1c1e" stroke-width="0.9" fill="none"/></svg>
        www.velorahealth.com
      </li>
    </ul>

    <address class="address">234 Anywhere St.,<br>Any City, US 123456</address>

    <div class="color-band"><span class="band-teal"></span><span class="band-purple"></span></div>
  </section>
</body>
</html>
```